Marbury 720 - Strategic Planning Consulting - Business Card Design

We need a business card design for a national public affairs consulting firm. We specialize in strategic planning for non-profit organizations including designing winning advocacy and communications campaigns. I'd like the design to be fresh and use the logo colors and the card should have rounded edges. On the back of the card I'd like a few words that help folks understand our services:

Strategic Planning
Advocacy Campaigns
Communications
Updates

Thank you to all the designers for your amazing work.  I wish I could select all of your talented designs.

Target Market(s)

The target customer is a CEO or VP of Public Policy or Communications.

Industry/Entity Type

Communications

Requirements
Must have
• Include:

LOGO

Loretta K. Vanhorn
President/CEO

4853 SE 17th Lane
Boca Raton, FL 33428

561.374.2096

Loretta@Marbury720.com
www.Marbury720.com

On back of card:
Strategic Planning
Advocacy Campaigns
Communications

```html
<!DOCTYPE html>
<html lang="en">
<head>
<meta charset="utf-8">
<title>Marbury 720 – Business Card</title>
<link rel="stylesheet" href="https://fonts.googleapis.com/css2?family=Open+Sans:wght@400;600;700&display=swap">
<style>
  :root {
    --purple: #9a68c4;
    --purple-soft: #b9a0d4;
    --purple-band: #a78bc6;
    --ink: #4a4a4a;
    --ink-soft: #6a6a6a;
    --ink-faint: #a9a9ad;
    --card-top: #f7f7f8;
    --card-bottom: #e9e9eb;
    --backdrop: #dcdcdf;
  }
  * { box-sizing: border-box; margin: 0; padding: 0; }
  html, body { width: 1200px; height: 1000px; overflow: hidden; }
  body {
    background: var(--backdrop);
    font-family: "Open Sans", Arial, sans-serif;
    color: var(--ink);
    position: relative;
  }
  .card {
    position: absolute;
    width: 640px;
    height: 366px;
    border-radius: 22px;
    overflow: hidden;
    background: linear-gradient(180deg, var(--card-top), var(--card-bottom));
    box-shadow: 0 10px 28px rgba(0,0,0,.18);
  }
  .card-band {
    position: absolute; left: 0; top: 0; right: 0; height: 20px;
    background: linear-gradient(90deg, var(--purple-band), var(--purple-soft));
  }
  .card-front { left: 90px; top: 80px; }
  .card-back { left: 470px; top: 550px; }

  /* front */
  .wordmark {
    position: absolute; top: 74px; left: 0; right: 0;
    display: flex; justify-content: center; align-items: center; gap: 12px;
  }
  .wordmark-name {
    font-size: 30px; font-weight: 400; color: var(--ink);
    letter-spacing: 3px; text-transform: uppercase;
  }
  .wordmark-square { width: 12px; height: 12px; background: var(--purple); }
  .divider {
    position: absolute; left: 0; right: 0; top: 150px; height: 1px;
    background: linear-gradient(90deg, transparent, rgba(0,0,0,.12), transparent);
  }
  .person { position: absolute; top: 170px; left: 0; right: 0; text-align: center; }
  .person-name { font-size: 22px; font-weight: 700; color: var(--ink); }
  .person-title { font-size: 15px; color: var(--ink-soft); margin-top: 2px; }
  .contact { position: absolute; font-size: 13px; color: var(--ink); }
  .contact-row { display: flex; align-items: flex-start; gap: 10px; margin-bottom: 12px; line-height: 18px; }
  .contact-icon { flex: none; width: 18px; height: 18px; display: flex; align-items: center; justify-content: center; }
  .contact-left { left: 52px; top: 262px; }
  .contact-right { left: 372px; top: 286px; font-size: 14px; }

  /* back */
  .services { position: absolute; left: 410px; top: 52px; list-style: none; }
  .services li {
    display: flex; align-items: center; gap: 10px;
    font-size: 14px; color: var(--ink-soft); margin-bottom: 16px;
  }
  .services li::before {
    content: ""; width: 9px; height: 9px; background: var(--purple);
  }
  .back-wordmark {
    position: absolute; left: 44px; bottom: 44px;
    display: flex; align-items: center; gap: 14px;
  }
  .back-wordmark-name {
    font-size: 40px; font-weight: 400; color: var(--ink-faint);
    letter-spacing: 5px; text-transform: uppercase; line-height: 1;
  }
  .back-wordmark-square { width: 16px; height: 16px; background: var(--purple-soft); }
</style>
</head>
<body>

<section class="card card-front" aria-label="Business card front">
  <div class="card-band"></div>
  <div class="wordmark">
    <span class="wordmark-square"></span>
    <span class="wordmark-name">Marbury 720</span>
  </div>
  <div class="divider"></div>
  <div class="person">
    <p class="person-name">Loretta K. Vanhorn</p>
    <p class="person-title">President/CEO</p>
  </div>
  <div class="contact contact-left">
    <div class="contact-row">
      <span class="contact-icon"><svg width="18" height="13" viewBox="0 0 18 13" aria-hidden="true"><rect x="0.5" y="0.5" width="17" height="12" fill="var(--purple)"/><path d="M1 1l8 6 8-6" fill="none" stroke="#fff" stroke-width="1.2"/></svg></span>
      <span>4853 SE 17th Lane<br>Boca Raton, FL 33428</span>
    </div>
    <div class="contact-row">
      <span class="contact-icon"><svg width="16" height="16" viewBox="0 0 24 24" aria-hidden="true"><path fill="var(--purple)" d="M6.6 10.8a15 15 0 0 0 6.6 6.6l2.2-2.2a1 1 0 0 1 1-.25 11.4 11.4 0 0 0 3.6.57 1 1 0 0 1 1 1V20a1 1 0 0 1-1 1A17 17 0 0 1 3 4a1 1 0 0 1 1-1h3.5a1 1 0 0 1 1 1c0 1.25.2 2.45.57 3.6a1 1 0 0 1-.25 1z"/></svg></span>
      <span>561.374.2096</span>
    </div>
  </div>
  <div class="contact contact-right">
    <div class="contact-row">
      <span class="contact-icon"><svg width="14" height="17" viewBox="0 0 14 17" aria-hidden="true"><path fill="var(--purple)" d="M0 0h9l5 5v12H0z"/><path fill="#fff" opacity=".5" d="M9 0v5h5z"/></svg></span>
      <span>www.Marbury720.com</span>
    </div>
    <div class="contact-row">
      <span class="contact-icon"><svg width="17" height="17" viewBox="0 0 24 24" aria-hidden="true"><text x="12" y="18" text-anchor="middle" font-size="20" font-family="Open Sans, sans-serif" fill="var(--purple)">@</text></svg></span>
      <span>Loretta@Marbury720.com</span>
    </div>
  </div>
</section>

<section class="card card-back" aria-label="Business card back">
  <div class="card-band"></div>
  <ul class="services">
    <li>Strategic Planning</li>
    <li>Advocacy Campaigns</li>
    <li>Communications</li>
  </ul>
  <div class="back-wordmark">
    <span class="back-wordmark-square"></span>
    <span class="back-wordmark-name">Marbury 720</span>
  </div>
</section>

</body>
</html>
```